Broadcaster,Conference Host,Facilitator

Looking for a business card and logo to create the Grant Ollerby brand .. Something with a slant towards radio and conference speaking
I like the idea of classic black white or grey but open to suggestions

Target Market(s)

Corporates

Industry/Entity Type

Business

Contact Information for Business Card

Grant Ollerby
Email : Grant.Ollerby@fenmail.co.uk
Mobile : +44 7700 384216
Twitter : @Grantollerby

Font styles to use
Serif
Decorative
Script

Requirements
Must have
• Feel classy and dynamic
Should not have
• Cartoons

```html
<!DOCTYPE html>
<html lang="en">
<head>
<meta charset="utf-8">
<title>Grant Ollerby – Business Card</title>
<link href="https://fonts.googleapis.com/css2?family=Josefin+Slab:wght@400;600&display=swap" rel="stylesheet">
<style>
  :root {
    --page: #d9d9d9;
    --card-black: #231f20;
    --brand-red: #e41b23;
    --text-white: #ffffff;
    --text-black: #1a1718;
  }
  html, body {
    margin: 0;
    padding: 0;
    width: 1200px;
    height: 900px;
    overflow: hidden;
    background: var(--page);
    font-family: "Josefin Slab", Georgia, serif;
  }
  .canvas {
    position: relative;
    width: 1200px;
    height: 900px;
  }
  .card {
    position: absolute;
    left: 280px;
    width: 640px;
    height: 372px;
    overflow: hidden;
    box-shadow: 0 6px 18px rgba(0,0,0,0.25);
  }
  .card--front { top: 40px; }
  .card--back  { top: 448px; background: var(--card-black); }

  .card__backdrop { position: absolute; inset: 0; }

  .brand-mark {
    position: absolute;
    border-radius: 50%;
  }
  .card--front .brand-mark {
    left: 87px; top: 45px;
    width: 116px; height: 116px;
    background: var(--card-black);
  }
  .card--back .brand-mark {
    left: 210px; top: 38px;
    width: 220px; height: 220px;
    background: var(--brand-red);
  }

  .brand-name {
    position: absolute;
    margin: 0;
    font-weight: 400;
    white-space: nowrap;
    text-align: center;
  }
  .card--front .brand-name {
    left: 0; width: 290px; top: 176px;
    font-size: 25px;
    color: var(--text-black);
  }
  .card--back .brand-name {
    left: 0; width: 640px; top: 276px;
    font-size: 46px;
    color: var(--text-white);
  }

  .contact {
    position: absolute;
    left: 340px;
    top: 100px;
  }
  .contact__name {
    margin: 0 0 10px;
    font-size: 30px;
    font-weight: 400;
    color: var(--brand-red);
    white-space: nowrap;
  }
  .contact__list {
    list-style: none;
    margin: 0;
    padding: 0;
  }
  .contact__item {
    display: flex;
    align-items: center;
    gap: 10px;
    height: 20px;
    margin-bottom: 2px;
    font-size: 16.5px;
    color: var(--text-white);
    white-space: nowrap;
  }
  .contact__icon {
    width: 14px;
    height: 14px;
    flex: none;
  }
  .contact__dot {
    width: 10px; height: 10px;
    margin: 0 2px;
    border-radius: 50%;
    background: var(--brand-red);
    flex: none;
  }
</style>
</head>
<body>
<main class="canvas">

  <section class="card card--front" aria-label="Business card, contact side">
    <svg class="card__backdrop" width="640" height="372" viewBox="0 0 640 372" aria-hidden="true">
      <rect width="640" height="372" fill="var(--brand-red)"/>
      <path d="M300 0 C255 90 250 220 330 372 L640 372 L640 0 Z" fill="var(--card-black)"/>
      <path d="M268 0 L284 0 C252 70 252 150 292 235 C240 165 244 75 268 0 Z" fill="var(--card-black)"/>
    </svg>
    <div class="brand-mark" aria-hidden="true"></div>
    <p class="brand-name">Grant Ollerby</p>

    <div class="contact">
      <h1 class="contact__name">Grant Ollerby</h1>
      <ul class="contact__list">
        <li class="contact__item">
          <svg class="contact__icon" viewBox="0 0 14 14" aria-hidden="true">
            <rect x="1" y="3" width="12" height="8.5" fill="none" stroke="var(--brand-red)" stroke-width="1.2"/>
            <path d="M1 3 L7 8 L13 3" fill="none" stroke="var(--brand-red)" stroke-width="1.2"/>
          </svg>
          Grant.Ollerby@fenmail.co.uk
        </li>
        <li class="contact__item">
          <svg class="contact__icon" viewBox="0 0 14 14" aria-hidden="true">
            <circle cx="7" cy="7" r="6" fill="none" stroke="var(--brand-red)" stroke-width="1.2"/>
            <path d="M4.6 4 L5.9 3.8 L6.5 5.5 L5.7 6.2 C6.1 7.1 6.9 7.9 7.8 8.3 L8.5 7.5 L10.2 8.1 L10 9.4 C7 9.8 4.2 7 4.6 4 Z" fill="var(--brand-red)"/>
          </svg>
          +44 7700 384216
        </li>
        <li class="contact__item">
          <span class="contact__dot" aria-hidden="true"></span>
          Grantollerby
        </li>
      </ul>
    </div>
  </section>

  <section class="card card--back" aria-label="Business card, brand side">
    <div class="brand-mark" aria-hidden="true"></div>
    <p class="brand-name">Grant Ollerby</p>
  </section>

</main>
</body>
</html>
```